Wine label design for my wife. Wine called "The Mirabel"

I need a wine label face lift of one of my premium wines in my collection. My wine sells in Harbor Lark's all over the States. My current label is called The Mirabel (my wife's name) and the illustration of her eyes is done by a well know artist from South Africa. I do not have to use this illustration and therefor I attached several pictures of her and her eyes, even when she was a little girl. The wine's also made in South Africa. This is a premium wine that we only sell 2000 bottles per year. The wine sells at 60 usd per bottle, The current label is too white. I also think her eyes should look more at the person buying it, than away from them.

Target Market(s)

Top end wine buyers

Font styles to use
Decorative
Script

Requirements
Must have
• 'The Mirabel' must be on the label
An illustration must be on the label
Basically all the info that's on the current label must be on by law. As per Sample
Nice to have
• Maybe some ideas of her whole face?
Should not have
• any gold colour

```html
<!DOCTYPE html>
<html lang="en">
<head>
<meta charset="utf-8">
<title>The Mirabel – Sauvignon Blanc Label</title>
<link rel="stylesheet" href="https://fonts.googleapis.com/css2?family=Pinyon+Script&family=Cinzel:wght@400;500&family=Cormorant+Garamond:ital,wght@1,500&display=swap">
<style>
  :root {
    --page-bg: #f4f2ee;
    --label-black: #0d0d0d;
    --label-black-soft: #1a1a1a;
    --silver: #cfd2d6;
    --silver-light: #f5f6f7;
    --silver-deep: #7c8187;
    --band-light: #8a8a8a;
    --band-dark: #262626;
    --portrait-light: #c9c9c9;
    --portrait-mid: #9a9a9a;
    --portrait-dark: #5c5c5c;
  }
  * { margin: 0; padding: 0; box-sizing: border-box; }
  html, body {
    width: 1200px;
    height: 450px;
    overflow: hidden;
    background: var(--page-bg);
  }
  .wine-label {
    position: absolute;
    left: 272px;
    top: 0;
    width: 655px;
    height: 450px;
    background: radial-gradient(ellipse at 50% 45%, var(--label-black-soft), var(--label-black) 75%);
    overflow: hidden;
  }
  .band {
    position: absolute;
    height: 7px;
    background: linear-gradient(90deg, transparent, var(--band-dark) 8%, var(--band-light) 30%, var(--band-dark) 48%, var(--band-dark) 52%, var(--band-light) 70%, var(--band-dark) 92%, transparent);
    opacity: 0.8;
  }
  .band--top { left: 29px; width: 597px; top: 23px; }
  .band--bottom { left: 29px; width: 597px; top: 432px; }
  .band--portrait-top { left: 150px; width: 359px; top: 208px; height: 6px; }
  .band--portrait-bottom { left: 150px; width: 359px; top: 337px; height: 6px; }

  .wine-name {
    position: absolute;
    top: 50px;
    left: 0;
    width: 100%;
    text-align: center;
    font-family: "Pinyon Script", cursive;
    font-weight: 400;
    font-size: 72px;
    line-height: 1;
    background: linear-gradient(180deg, var(--silver-light) 0%, var(--silver) 40%, var(--silver-deep) 70%, var(--silver) 100%);
    -webkit-background-clip: text;
    background-clip: text;
    color: transparent;
  }
  .varietal {
    position: absolute;
    top: 136px;
    left: 0;
    width: 100%;
    text-align: center;
    font-family: "Cinzel", serif;
    font-size: 19px;
    line-height: 22px;
    letter-spacing: 1px;
    color: var(--silver);
  }
  .since {
    position: absolute;
    top: 158px;
    left: 0;
    width: 100%;
    display: flex;
    justify-content: center;
    align-items: center;
    gap: 6px;
    font-family: "Cormorant Garamond", serif;
    font-style: italic;
    font-weight: 500;
    font-size: 20px;
    line-height: 24px;
    font-variant-numeric: lining-nums;
    color: var(--silver);
  }
  .since::before, .since::after {
    content: "";
    width: 50px;
    height: 1px;
    background: var(--silver);
  }
  .portrait {
    position: absolute;
    left: 131px;
    top: 220px;
    width: 392px;
    height: 111px;
    background: linear-gradient(90deg, var(--portrait-dark) 0%, var(--portrait-light) 12%, var(--portrait-mid) 40%, var(--portrait-light) 55%, var(--portrait-mid) 85%, var(--portrait-dark) 100%);
  }
  .winery {
    position: absolute;
    top: 356px;
    left: 0;
    width: 100%;
    text-align: center;
    font-family: "Cinzel", serif;
    font-size: 17px;
    line-height: 22px;
    letter-spacing: 0.5px;
    color: var(--silver);
  }
  .divider {
    position: absolute;
    top: 391px;
    left: 290px;
    width: 75px;
    height: 1px;
    background: linear-gradient(90deg, transparent, var(--silver), transparent);
  }
  .origin {
    position: absolute;
    top: 410px;
    left: 0;
    width: 100%;
    text-align: center;
    font-family: "Cinzel", serif;
    font-weight: 500;
    font-size: 10px;
    line-height: 14px;
    letter-spacing: 4px;
    color: var(--silver);
  }
</style>
</head>
<body>
  <main class="wine-label">
    <div class="band band--top"></div>
    <h1 class="wine-name">The Mirabel</h1>
    <p class="varietal">SAUVIGNON BLANC</p>
    <p class="since">Since 2017</p>
    <div class="band band--portrait-top"></div>
    <div class="portrait" role="img" aria-label="Black and white portrait strip of the wife's eyes"></div>
    <div class="band band--portrait-bottom"></div>
    <p class="winery">DAWID VENTER WINES</p>
    <div class="divider"></div>
    <p class="origin">SOUTH AFRICA</p>
    <div class="band band--bottom"></div>
  </main>
</body>
</html>
```